Business Card Design

Company name is: Tallowmere Rescue Skills, LLC. We teach CPR/AED, First Aid, Bloodborne Pathogens and other health and safety classes. Looking for an eye-catching, progressive, cutting edge design.

Industry/Entity Type

Health

Contact Information for Business Card

Dale Fenwarick (555.218.4703)
Nora Quillstead (555.276.9148)
email is info@tallowmererescue.example
website is www.TallowmereRescue.example

```html
<!DOCTYPE html>
<html lang="en">
<head>
<meta charset="utf-8">
<title>Tallowmere Rescue Skills, LLC — Business Card</title>
<link rel="stylesheet" href="https://fonts.googleapis.com/css2?family=Open+Sans:wght@400;600;700&display=swap">
<style>
  :root {
    --card-bg: #ffffff;
    --brand-blue: #3aaefc;
    --brand-red: #e8000b;
    --rule-red: #f08a8a;
    --ink: #111111;
  }
  html, body {
    margin: 0;
    padding: 0;
    overflow: hidden;
    background: var(--card-bg);
  }
  .card {
    position: relative;
    width: 1200px;
    height: 704px;
    background: var(--card-bg);
    font-family: "Open Sans", Arial, sans-serif;
    overflow: hidden;
  }
  .brand-mark {
    position: absolute;
    left: 0;
    top: 0;
  }
  .brand-name {
    position: absolute;
    left: 273px;
    width: 654px;
    top: 220px;
    height: 68px;
    border-top: 1px solid var(--rule-red);
    border-bottom: 1px solid var(--rule-red);
    box-sizing: border-box;
    display: flex;
    align-items: center;
    justify-content: center;
    margin: 0;
    font-size: 42px;
    font-weight: 400;
    letter-spacing: 0.5px;
    color: var(--brand-blue);
    white-space: nowrap;
  }
  .pulse-band {
    position: absolute;
    left: 0;
    top: 354px;
    width: 1200px;
    height: 13px;
    background: var(--brand-blue);
  }
  .services {
    position: absolute;
    left: 230px;
    top: 378px;
    margin: 0;
    font-size: 28px;
    font-weight: 600;
    color: var(--brand-red);
    white-space: nowrap;
    letter-spacing: 0.2px;
  }
  .contacts {
    position: absolute;
    left: 0;
    width: 1200px;
    top: 462px;
    text-align: center;
    font-size: 31px;
    line-height: 59px;
    font-weight: 600;
  }
  .contact-name { color: var(--brand-blue); font-weight: 400; }
  .contact-phone { color: var(--ink); }
  .web-line {
    position: absolute;
    left: 0;
    width: 1200px;
    top: 610px;
    text-align: center;
    font-size: 30px;
    font-weight: 600;
    color: var(--ink);
    white-space: nowrap;
  }
  .label { color: var(--brand-blue); font-weight: 400; }
  .divider { color: var(--brand-red); font-weight: 400; padding: 0 6px; }
</style>
</head>
<body>
  <div class="card">
    <svg class="brand-mark" width="1200" height="220" aria-hidden="true">
      <circle cx="599" cy="110" r="78" fill="var(--brand-red)"/>
    </svg>

    <h1 class="brand-name">TALLOWMERE RESCUE SKILLS, LLC.</h1>

    <div class="pulse-band"></div>

    <p class="services">CPR/AED, FIRST AID &amp; BLOODBORNE PATHOGEN TRAINING</p>

    <div class="contacts">
      <div><span class="contact-name">Dale Fenwarick</span> <span class="contact-phone">- 555.218.4703</span></div>
      <div><span class="contact-name">Nora Quillstead</span> <span class="contact-phone">- 555.276.9148</span></div>
    </div>

    <div class="web-line">
      <span class="label">Email:</span> info@tallowmererescue.example<span class="divider">|</span><span class="label">Web:</span> www.tallowmererescue.example
    </div>
  </div>
</body>
</html>
```